Powerpoint Presentation

We have a basic 8 page presentation that we would like created on powerpoint. The presentation is very simple dot points and we would like to jazz it up with relevant photos/images relating to the topic on each page.

The topic of the presentation is 'creating a powerful presence and knowing your personal brand' (see attached files).

Target Market(s)

Business women

Requirements
Must have
• Images that match the content on each page

```html
<!DOCTYPE html>
<html lang="en">
<head>
<meta charset="utf-8">
<title>Presence, Positioning, Voice and Language</title>
<link rel="stylesheet" href="https://fonts.googleapis.com/css2?family=Kanit:wght@300&family=Tinos&display=swap">
<style>
  :root {
    --teal-deep: #1f4655;
    --teal-mid: #2d5a69;
    --teal-light: #8fb0b5;
    --sky-haze: #6d8f97;
    --kit-red: #c8483f;
    --kit-red-dark: #8e3a36;
    --track-dark: #2a3a40;
    --glow-text: #c9f7f6;
    --glow-shadow: #2fd3d8;
    --brand-orange: #f06a25;
    --footer-text: #111111;
  }
  * { margin: 0; padding: 0; box-sizing: border-box; }
  html, body { width: 1200px; height: 900px; overflow: hidden; background: var(--teal-deep); }
  .slide {
    position: relative;
    width: 1200px;
    height: 900px;
    overflow: hidden;
    background: linear-gradient(180deg, var(--teal-mid) 0%, var(--teal-deep) 100%);
    font-family: "Kanit", sans-serif;
  }
  .hero-photo {
    position: absolute;
    left: 420px;
    top: 0;
    width: 780px;
    height: 845px;
    background:
      radial-gradient(ellipse 28% 30% at 52% 48%, var(--kit-red) 0%, rgba(200, 72, 63, 0.6) 55%, rgba(200, 72, 63, 0) 100%),
      radial-gradient(ellipse 22% 22% at 50% 72%, var(--kit-red-dark) 0%, rgba(142, 58, 54, 0) 100%),
      radial-gradient(ellipse 55% 45% at 62% 22%, var(--teal-light) 0%, rgba(143, 176, 181, 0) 100%),
      linear-gradient(180deg, var(--sky-haze) 0%, #4d7480 45%, #3b5a63 65%, var(--track-dark) 100%);
    -webkit-mask-image: linear-gradient(90deg, transparent 0%, #000 28%, #000 100%);
    mask-image: linear-gradient(90deg, transparent 0%, #000 28%, #000 100%);
  }
  .brand {
    position: absolute;
    left: 15px;
    top: 15px;
  }
  .brand-mark {
    display: block;
    width: 72px;
    height: 72px;
    border-radius: 50%;
    background: var(--brand-orange);
  }
  .brand-name {
    display: block;
    margin-top: 16px;
    color: var(--brand-orange);
    font-size: 35px;
    font-weight: 300;
    line-height: 1;
    letter-spacing: 0.5px;
  }
  .topic {
    position: absolute;
    transform: translateX(-50%);
    white-space: nowrap;
    color: var(--glow-text);
    font-weight: 300;
    line-height: 1;
    text-shadow: 0 0 6px var(--glow-shadow), 0 0 14px var(--glow-shadow);
  }
  .topic--presence { left: 338px; top: 228px; font-size: 74px; letter-spacing: 2px; }
  .topic--positioning { left: 343px; top: 392px; font-size: 74px; letter-spacing: 2px; }
  .topic--voice { left: 352px; top: 565px; font-size: 60px; letter-spacing: 3px; }
  .photo-credit {
    position: absolute;
    left: 0;
    bottom: 0;
    width: 1200px;
    height: 55px;
    background: var(--brand-orange);
    color: var(--footer-text);
    font-family: "Tinos", serif;
    font-size: 17px;
    line-height: 55px;
    padding-left: 14px;
    white-space: nowrap;
  }
</style>
</head>
<body>
  <main class="slide">
    <div class="hero-photo" role="img" aria-label="Photo of a female sprinter in a red running kit crouched in the starting position on an athletics track, looking up ahead"></div>

    <div class="brand">
      <span class="brand-mark"></span>
      <span class="brand-name">beyond shared walls</span>
    </div>

    <h1 class="topic topic--presence">Presence</h1>
    <h2 class="topic topic--positioning">Positioning</h2>
    <h2 class="topic topic--voice">Voice and Language</h2>

    <footer class="photo-credit">Photo Source: http://janemarlowruns.example.com/2012/08/27/start-running-even-if-you-need-a-bucket/</footer>
  </main>
</body>
</html>
```